Organic rose water based skincare line in need of product label and packaging design

We are looking for a simple, clean, modern labeling and packaging design for 2 of our products. Our brand's demographic is upscale females ages 20-40. We want our packaging to be very minimalistic, and instagramable.

Product #1: Rose water facial spray "Lilac Mist"
Product #2: Rose water facial toner "The Late Hour"

Please see attached images for our current logo and label design. We have also added some images that inspire our branding.

Target Market(s)

trendy woman ages 20-40

Industry/Entity Type

Skin Care Product

Font styles to use
Serif
Sans Serif

Colors

Designer to choose only greyscale colors for use in the design.

Requirements
Must have
• Must have our logo, bottle size, product name on front and how to use and ingredient on the back. Please see project description and attached images for more information.
Should not have
• Too much going on or too many colors.

```html
<!DOCTYPE html>
<html lang="en">
<head>
<meta charset="utf-8">
<title>Bloom Study – The Late Hour toner labels</title>
<link href="https://fonts.googleapis.com/css2?family=Josefin+Sans:wght@300;400&family=Montserrat:wght@400;600;700&family=Mrs+Saint+Delafield&display=swap" rel="stylesheet">
<style>
  :root {
    --backdrop: #f1f1f1;
    --label: #ffffff;
    --ink: #3d3d3d;
    --ink-soft: #6a6a6a;
    --rule: #8a8a8a;
    --blush: #e9a497;
    --art: #ececec;
    --edge: #dcdcdc;
  }
  * { box-sizing: border-box; margin: 0; padding: 0; }
  html, body { width: 1200px; height: 611px; overflow: hidden; background: var(--backdrop); }
  .canvas { position: relative; width: 1200px; height: 611px; font-family: "Montserrat", sans-serif; color: var(--ink); }

  .label {
    position: absolute; background: var(--label);
    display: flex; flex-direction: column; align-items: center; text-align: center;
  }
  .label--tall { width: 200px; height: 460px; top: 76px; border-radius: 20px; box-shadow: 0 2px 10px rgba(0,0,0,.12); padding: 22px 16px 18px; }
  .label--front { left: 40px; }
  .label--back { left: 262px; }

  .wrap-label { position: absolute; left: 500px; top: 92px; width: 660px; height: 428px; background: var(--label); display: flex; box-shadow: 0 2px 10px rgba(0,0,0,.12); }
  .panel { flex: 1; display: flex; flex-direction: column; align-items: center; text-align: center; padding: 26px 12px 18px; border-right: 1px solid var(--edge); }
  .panel:last-child { border-right: none; }

  .brand { font-family: "Montserrat", sans-serif; font-weight: 400; font-size: 20px; line-height: 0.9; color: var(--ink-soft); text-transform: lowercase; }
  .rule { width: 36px; height: 1px; background: var(--rule); margin: 22px 0 16px; }
  .rule--close { margin: 10px 0 12px; }
  .title { font-family: "Josefin Sans", sans-serif; font-weight: 300; font-size: 34px; line-height: 1.02; letter-spacing: 2px; color: var(--ink); text-transform: uppercase; }
  .subtitle { font-size: 9px; color: var(--ink-soft); margin-top: 8px; }
  .subtitle--blush { color: var(--blush); }
  .script { font-family: "Mrs Saint Delafield", cursive; font-size: 28px; color: var(--blush); margin-top: 10px; line-height: 1; }
  .benefits { list-style: none; font-size: 11px; line-height: 1.45; color: var(--ink-soft); margin-top: 4px; }
  .size { font-size: 10px; color: var(--ink); margin-top: auto; }

  .copy-head { font-size: 10px; font-weight: 700; margin-top: 8px; }
  .copy { font-size: 9.5px; line-height: 1.4; margin-top: 2px; }
  .maker { font-size: 7.5px; line-height: 1.4; margin-top: auto; }
  .maker strong { font-weight: 700; }

  .art { background: var(--art); border-radius: 4px; }
  .art--rose-back { width: 90px; height: 100px; margin-top: 14px; }
  .art--rose-side { width: 110px; height: 150px; margin-top: 18px; }
  .art--rose-mid { width: 60px; height: 92px; margin-top: 10px; }
  .symbols { display: flex; gap: 5px; margin-top: 8px; }
  .symbols span { width: 11px; height: 11px; border: 1px solid var(--ink); border-radius: 2px; }
  .panel--side .symbols { align-self: flex-start; margin-top: auto; }
</style>
</head>
<body>
<main class="canvas">

  <section class="label label--tall label--front">
    <p class="brand">bloom<br>study</p>
    <span class="rule"></span>
    <h1 class="title">The<br>Late<br>Hour</h1>
    <p class="subtitle">organic rose facial toner</p>
    <p class="script">witchhazel/rose</p>
    <ul class="benefits">
      <li>tightens skin</li><li>shrinks pores</li><li>prevents acne</li><li>treats discoloration</li><li>removes impurities</li>
    </ul>
    <p class="size">4 oz / 120 mL</p>
  </section>

  <section class="label label--tall label--back">
    <div class="art art--rose-back" role="img" aria-label="Single-line drawing of a rose on a stem"></div>
    <p class="copy-head">Directions:</p>
    <p class="copy">Shake well. Apply a small amount of toner to a clean cotton pad and gently sweep over your face and neck.</p>
    <p class="copy-head">Ingredients:</p>
    <p class="copy">Lorem ipsum dolor sit amet, consectetuer adipiscing elit, sed diam nonummy nibh euismod tincidunt ut laoreet dolore.</p>
    <p class="maker"><strong>MANUFACTURED BY:</strong><br>BLOOM STUDY<br>Street Address, City, UT Zipcode</p>
  </section>

  <section class="wrap-label">
    <div class="panel panel--side">
      <p class="script">witchhazel/rose</p>
      <ul class="benefits">
        <li>tightens skin</li><li>shrinks pores</li><li>prevents acne</li><li>treats discoloration</li><li>removes impurities</li>
      </ul>
      <div class="art art--rose-side" role="img" aria-label="Single-line drawing of a rose on a stem"></div>
      <div class="symbols" aria-label="Care and recycling symbols"><span></span><span></span><span></span></div>
    </div>

    <div class="panel">
      <p class="brand">bloom<br>study</p>
      <span class="rule" style="margin-top:70px"></span>
      <h2 class="title">The<br>Late<br>Hour</h2>
      <p class="subtitle subtitle--blush">organic rose facial toner</p>
      <span class="rule rule--close"></span>
      <p class="size">4 oz/120 mL</p>
    </div>

    <div class="panel">
      <p class="copy-head" style="margin-top:0">Directions:</p>
      <p class="copy">Shake well. Apply a small amount of toner to a clean cotton pad and gently sweep over your face and neck.</p>
      <p class="copy-head">Ingredients:</p>
      <p class="copy">Lorem ipsum dolor sit amet, consectetuer adipiscing elit, sed diam nonummy nibh euismod tincidunt ut laoreet dolore.</p>
      <div class="art art--rose-mid" role="img" aria-label="Single-line drawing of a rose on a stem"></div>
      <div class="symbols" aria-label="Care and recycling symbols"><span></span><span></span><span></span></div>
      <p class="maker"><strong>MANUFACTURED BY:</strong><br>BLOOM STUDY<br>Street Address,<br>City, UT Zipcode</p>
    </div>

    <div class="panel">
      <p class="brand">bloom<br>study</p>
      <span class="rule" style="margin-top:70px"></span>
      <h2 class="title">The<br>Late<br>Hour</h2>
      <p class="subtitle subtitle--blush">organic rose facial toner</p>
      <span class="rule rule--close"></span>
      <p class="size">4 oz/120 mL</p>
    </div>
  </section>

</main>
</body>
</html>
```